Limbcraft Arbor Crew Bill Board Design

We are a high class full service tree company who specializes in artistic thinning and shaping of trees in Arizona. We want to re brand our company to catch our audiences attention and hook them into calling our company on the spot. We’ve been in business for 30 years and have never truly branded our company. We want our shirts trucks and billboards to match as well as our mailing advertisement so our clientele can recognize us immediately. We are starting with our billboard first and will be following with truck and shirt designs next. Attached is a example of what we are looking for and what we’ve had designed so far. This just isn’t good enough and needs revamped if at all posssible.
- Stencil

```html
<!DOCTYPE html>
<html lang="en">
<head>
<meta charset="utf-8">
<title>Limbcraft Arbor Crew Billboard</title>
<link href="https://fonts.googleapis.com/css2?family=Roboto+Condensed:wght@700&family=Oswald:wght@500;700&family=Dancing+Script:wght@600&display=swap" rel="stylesheet">
<style>
  :root {
    --page-bg: #e9edf1;
    --board-dark: #24262b;
    --brand-green: #1fa84f;
    --brand-gold: #c49a2c;
    --text-white: #ffffff;
    --foliage-deep: #4f7a2e;
    --foliage-light: #9cbf6a;
    --sky-pale: #dfe9ec;
  }
  * { margin: 0; padding: 0; box-sizing: border-box; }
  html, body {
    width: 1200px;
    height: 900px;
    overflow: hidden;
    background: var(--page-bg);
  }
  .billboard {
    position: absolute;
    left: 50px;
    top: 170px;
    width: 1100px;
    height: 560px;
    background: var(--board-dark);
    overflow: hidden;
    box-shadow: 0 10px 30px rgba(0,0,0,0.18);
  }
  .billboard-shapes {
    position: absolute;
    inset: 0;
  }
  .brand {
    position: absolute;
    left: 560px;
    top: 160px;
    display: flex;
    align-items: center;
    gap: 16px;
    white-space: nowrap;
  }
  .brand-dot {
    width: 52px;
    height: 52px;
    border-radius: 50%;
    background: var(--brand-green);
    flex: none;
  }
  .brand-text { display: flex; flex-direction: column; }
  .brand-name {
    font-family: "Oswald", sans-serif;
    font-weight: 500;
    font-size: 30px;
    letter-spacing: 1px;
    color: var(--text-white);
    line-height: 1.1;
  }
  .brand-tagline {
    font-family: "Dancing Script", cursive;
    font-weight: 600;
    font-size: 18px;
    color: var(--text-white);
    margin-left: 60px;
  }
  .experience-badge {
    position: absolute;
    right: 48px;
    top: 30px;
    text-align: center;
    font-family: "Oswald", sans-serif;
    font-weight: 700;
    line-height: 1;
    white-space: nowrap;
  }
  .experience-label { color: var(--brand-green); font-size: 22px; letter-spacing: 2px; }
  .experience-years-number { color: var(--brand-gold); font-size: 58px; margin: 4px 0; }
  .experience-years-label { color: var(--brand-green); font-size: 18px; letter-spacing: 1px; }
  .phone {
    position: absolute;
    left: 540px;
    top: 272px;
    font-family: "Roboto Condensed", sans-serif;
    font-weight: 700;
    font-size: 92px;
    line-height: 1;
    color: var(--text-white);
    letter-spacing: -1px;
    white-space: nowrap;
  }
  .headline {
    position: absolute;
    left: 560px;
    top: 422px;
    font-family: "Roboto Condensed", sans-serif;
    font-weight: 700;
    color: var(--text-white);
    text-transform: uppercase;
    line-height: 1.05;
    white-space: nowrap;
  }
  .headline-service { font-size: 40px; }
  .headline-region { font-size: 56px; margin-top: 6px; }
</style>
</head>
<body>
  <main class="billboard">
    <svg class="billboard-shapes" width="1100" height="560" viewBox="0 0 1100 560">
      <defs>
        <linearGradient id="foliageFill" x1="0" y1="0" x2="0.6" y2="1">
          <stop offset="0" stop-color="var(--sky-pale)"/>
          <stop offset="0.35" stop-color="var(--foliage-light)"/>
          <stop offset="1" stop-color="var(--foliage-deep)"/>
        </linearGradient>
      </defs>
      <polygon class="photo-area" points="0,0 300,0 540,560 0,560" fill="url(#foliageFill)" role="img" aria-label="Photo of an arborist in a bucket lift pruning a tree with a pole saw"/>
      <polygon class="gold-divider" points="300,0 322,0 562,560 540,560" fill="var(--brand-gold)"/>
      <polygon class="service-band" points="493,400 1100,400 1100,560 562,560" fill="var(--brand-green)"/>
    </svg>

    <div class="brand">
      <span class="brand-dot"></span>
      <div class="brand-text">
        <span class="brand-name">Limbcraft Arbor Crew</span>
        <span class="brand-tagline">Providing Expert Tree Care</span>
      </div>
    </div>

    <div class="experience-badge">
      <div class="experience-label">EXPERIENCE</div>
      <div class="experience-years-number">30</div>
      <div class="experience-years-label">YEARS</div>
    </div>

    <div class="phone">602-555-0147</div>

    <div class="headline">
      <div class="headline-service">Artistic Thinning &amp; Shaping</div>
      <div class="headline-region">Of Trees in Arizona</div>
    </div>
  </main>
</body>
</html>
```